Project Title:
Dental Implant Overdenture Flyer (Retirement Village Target)
Objective:
Create a clean, trustworthy, and reassuring flyer aimed at older adults (60–85 years old) who struggle with loose dentures. The goal is to educate them about implant-retained “clip-on” dentures and encourage them to book a consultation.
Tone & Feel:
Warm, caring, non-intimidating
Premium but not “salesy”
Medical but easy to understand
Focus on improving quality of life (confidence, eating, comfort)
Target Audience:
Retirees / pensioners
Existing denture wearers
People frustrated with loose or uncomfortable dentures
Key Message:
“You don’t have to live with loose dentures anymore.”
Design Style:
Clean, minimal, modern
Soft colours (blues, greens, warm neutrals)
Easy-to-read large font
High contrast for older eyes
Avoid clutter
Imagery Suggestions:
Smiling older adults (natural, not stocky/overly staged)
Before/after lifestyle (eating, laughing, socialising)
Simple diagram showing denture clipping onto implants
Avoid graphic surgical images
Layout Suggestions:
A5 or DL flyer
Clear sections with headings
Icons for benefits
Strong call-to-action at bottom
HEADLINE (big and bold)
Tired of Loose Dentures?
Discover Secure “Clip-On” Teeth
🔹 PROBLEM SECTION
Do your dentures:
Slip or move when eating?
Make it hard to chew certain foods?
Feel uncomfortable or loose?
Affect your confidence when speaking or smiling?
You’re not alone — and there is a better solution.
🔹 SOLUTION SECTION
Implant-Retained “Clip-On” Dentures
We can secure your denture using just 2 dental implants, allowing your teeth to:
✔ Stay firmly in place
✔ Improve your ability to eat
✔ Feel more comfortable
✔ Boost your confidence
🔹 SIMPLE EXPLANATION (very important)
Small titanium implants are gently placed in the jaw.
Your denture then clips securely onto them, stopping movement.
🔹 PRICE SECTION (highlight this clearly)
$12,000
Includes:
2 dental implants
A brand new custom overdenture
Does not include sedation or extractions (if needed)
🔹 SEDATION
Sedation is available for comfort.
If you hold a pensioner card, you may receive a significant Vantacor rebate, often resulting in minimal out-of-pocket costs for sedation.
🔹 TRUST / REASSURANCE
Experienced implant clinician
Gentle, patient-focused care
Modern technology and techniques
🔹 CALL TO ACTION (VERY IMPORTANT)
Book a Free Consultation
📞 Call: 08 9351 4276
🌐 Visit: www.bravonclinic.com.au
📍 Located near Tallowmere shopping centre
🔹 OPTIONAL TAGLINE
Eat Better. Feel Better. Smile with Confidence Again.
Please include some photos to illustrate what a clip on denture looks like with two implants.

```html
<!DOCTYPE html>
<html lang="en">
<head>
<meta charset="utf-8">
<title>Clip-On Dentures Flyer</title>
<link rel="stylesheet" href="https://fonts.googleapis.com/css2?family=Poppins:wght@500;600;700;800&display=swap">
<style>
  :root {
    --backdrop: #545454;
    --paper: #ffffff;
    --teal-deep: #0096b4;
    --teal-bright: #1fd6cc;
    --ink: #111111;
    --gum: #f08a8f;
    --gum-light: #f9c3c4;
    --photo-dark: #2a2a2a;
    --photo-light: #e9e4df;
  }
  * { margin: 0; padding: 0; box-sizing: border-box; }
  html, body { width: 879px; height: 1200px; overflow: hidden; background: var(--backdrop); }
  body { font-family: "Poppins", sans-serif; color: var(--ink); position: relative; }
  .flyer { position: absolute; left: 124px; top: 113px; width: 631px; height: 975px; background: var(--paper); overflow: hidden; }
  .abs { position: absolute; }

  .brand { left: 47px; top: 70px; display: flex; align-items: center; gap: 10px; }
  .brand-dot { width: 30px; height: 30px; border-radius: 50%; background: var(--teal-deep); }
  .brand-name { font-weight: 600; font-size: 22px; letter-spacing: 4px; color: var(--teal-deep); }

  .denture-photo { left: 368px; top: 0; width: 263px; height: 475px; z-index: 2; }

  .headline { left: 49px; top: 158px; font-weight: 800; font-size: 69px; line-height: 58px; letter-spacing: -1px; z-index: 3; }
  .headline .l1 { color: var(--teal-deep); display: block; }
  .headline .l2 { color: var(--ink); display: block; }
  .headline .l3 { color: var(--teal-bright); display: block; }
  .subhead { left: 51px; top: 343px; font-weight: 700; font-size: 23px; z-index: 3; }

  .problem-box { left: 35px; top: 387px; width: 562px; height: 129px; background: var(--teal-deep); border-radius: 8px; color: #fff; z-index: 1; }
  .problem-title { left: 13px; top: 7px; font-weight: 700; font-size: 19px; }
  .problem-item { display: flex; align-items: center; gap: 9px; font-weight: 500; font-size: 15px; line-height: 18px; }
  .problem-icon { width: 31px; height: 31px; border-radius: 4px; background: var(--teal-bright); flex: none; display: flex; align-items: center; justify-content: center; }

  .solution-title { left: 47px; top: 526px; font-weight: 700; font-size: 20px; line-height: 23px; color: var(--teal-deep); }
  .solution-body { left: 47px; top: 579px; font-weight: 700; font-size: 14.5px; line-height: 19px; }
  .divider { left: 363px; top: 526px; width: 1.5px; height: 98px; background: var(--teal-deep); }
  .benefits { left: 376px; top: 526px; list-style: none; }
  .benefits li, .trust li { display: flex; align-items: center; gap: 8px; font-weight: 500; }
  .benefits li { font-size: 15.5px; height: 23.5px; }

  .explain { left: 47px; top: 633px; font-weight: 500; font-size: 11.8px; line-height: 15.5px; }

  .price-band { left: 35px; top: 676px; width: 562px; height: 52px; background: var(--teal-bright); border-radius: 6px; color: #fff; }
  .price { left: 17px; top: 4px; font-weight: 700; font-size: 35px; }
  .price-note { font-weight: 700; font-size: 11px; line-height: 15px; text-align: center; top: 11px; }

  .sedation-title { left: 47px; top: 734px; font-weight: 700; font-size: 20px; color: var(--teal-deep); }
  .sedation-body { left: 47px; top: 763px; font-weight: 500; font-size: 11.5px; line-height: 15px; z-index: 3; }
  .trust { left: 47px; top: 805px; list-style: none; }
  .trust li { font-size: 13.5px; height: 21.5px; }

  .phone { left: 47px; top: 889px; display: flex; align-items: center; gap: 3px; font-weight: 800; font-size: 30px; }
  .web { left: 49px; top: 926px; font-weight: 700; font-size: 18px; }
  .web span { color: var(--teal-deep); }

  .clinician-photo { left: 385px; top: 743px; width: 223px; height: 232px; }
  .clinician-name { left: 416px; top: 839px; font-weight: 700; font-size: 14px; line-height: 12px; color: var(--teal-deep); z-index: 2; }
</style>
</head>
<body>
<main class="flyer">
  <div class="abs brand"><span class="brand-dot"></span><span class="brand-name">BRAVON CLINIC</span></div>

  <svg class="abs denture-photo" viewBox="0 0 263 475" role="img" aria-label="Close-up of upper and lower denture with pink gums and white teeth">
    <defs>
      <radialGradient id="gumGlow" cx="0.6" cy="0.45" r="0.7">
        <stop offset="0" stop-color="#ffffff"/>
        <stop offset="0.35" stop-color="var(--gum-light)"/>
        <stop offset="1" stop-color="var(--gum)"/>
      </radialGradient>
    </defs>
    <path d="M0 0 H263 V472 C150 472 82 440 80 380 V240 C40 232 8 190 0 120 Z" fill="url(#gumGlow)"/>
  </svg>

  <h1 class="abs headline"><span class="l1">TIRED</span><span class="l2">OF LOOSE</span><span class="l3">DENTURES?</span></h1>
  <p class="abs subhead">Discover Secure “Clip-On” Teeth</p>

  <section class="abs problem-box">
    <h2 class="abs problem-title">DO YOUR DENTURES:</h2>
    <div class="abs problem-item" style="left:12px;top:38px"><span class="problem-icon"><svg width="18" height="14" viewBox="0 0 18 14"><path d="M2 4 Q9 -1 16 4 M2 10 Q9 15 16 10" stroke="#fff" stroke-width="1.6" fill="none"/></svg></span>Slip or move<br>when eating?</div>
    <div class="abs problem-item" style="left:222px;top:38px"><span class="problem-icon"><svg width="18" height="14" viewBox="0 0 18 14"><path d="M2 4 Q9 -1 16 4 M2 10 Q9 15 16 10" stroke="#fff" stroke-width="1.6" fill="none"/></svg></span>Feel uncomfortable<br>or loose?</div>
    <div class="abs problem-item" style="left:12px;top:82px"><span class="problem-icon"><svg width="18" height="14" viewBox="0 0 18 14"><path d="M2 4 Q9 -1 16 4 M2 10 Q9 15 16 10" stroke="#fff" stroke-width="1.6" fill="none"/></svg></span>Make it hard to<br>chew certain foods?</div>
    <div class="abs problem-item" style="left:222px;top:82px"><span class="problem-icon"><svg width="18" height="14" viewBox="0 0 18 14"><path d="M4 8 Q9 13 14 8" stroke="#fff" stroke-width="1.6" fill="none"/></svg></span>Affect your confidence<br>when speaking or smiling?</div>
  </section>

  <h2 class="abs solution-title">IMPLANT-RETAINED<br>“CLIP-ON” DENTURES</h2>
  <p class="abs solution-body">We Can Secure Your Denture Using Just<br>2 Dental Implants, Allowing Your Teeth To:</p>
  <div class="abs divider"></div>
  <ul class="abs benefits">
    <li><svg width="13" height="13" viewBox="0 0 14 14"><circle cx="7" cy="7" r="6" stroke="var(--teal-deep)" stroke-width="1.5" fill="none"/><path d="M4 7 l2 2 l4-4" stroke="var(--teal-deep)" stroke-width="1.6" fill="none"/></svg>Stay firmly in place</li>
    <li><svg width="13" height="13" viewBox="0 0 14 14"><circle cx="7" cy="7" r="6" stroke="var(--teal-deep)" stroke-width="1.5" fill="none"/><path d="M4 7 l2 2 l4-4" stroke="var(--teal-deep)" stroke-width="1.6" fill="none"/></svg>Improve your ability to eat</li>
    <li><svg width="13" height="13" viewBox="0 0 14 14"><circle cx="7" cy="7" r="6" stroke="var(--teal-deep)" stroke-width="1.5" fill="none"/><path d="M4 7 l2 2 l4-4" stroke="var(--teal-deep)" stroke-width="1.6" fill="none"/></svg>Feel more comfortable</li>
    <li><svg width="13" height="13" viewBox="0 0 14 14"><circle cx="7" cy="7" r="6" stroke="var(--teal-deep)" stroke-width="1.5" fill="none"/><path d="M4 7 l2 2 l4-4" stroke="var(--teal-deep)" stroke-width="1.6" fill="none"/></svg>Boost your confidence</li>
  </ul>

  <p class="abs explain">Small Titanium Implants are Gently Placed in The Jaw.<br>Your Denture Then Clips Securely Onto Them, Stopping Movement.</p>

  <section class="abs price-band">
    <div class="abs price">$12,000</div>
    <p class="abs price-note" style="left:180px;width:200px">2 Dental Implants<br>A Brand New Custom Overdenture</p>
    <p class="abs price-note" style="left:397px;width:155px">Does Not Include Sedation<br>Or Extractions (If Needed)</p>
  </section>

  <h2 class="abs sedation-title">Sedation is Available for Comfort.</h2>
  <p class="abs sedation-body">If you hold a pensioner card, you may receive a significant Vantacor<br>rebate, often resulting in minimal out-of-pocket costs for sedation.</p>

  <ul class="abs trust">
    <li><svg width="12" height="12" viewBox="0 0 14 14"><circle cx="7" cy="7" r="6" stroke="var(--teal-deep)" stroke-width="1.5" fill="none"/><path d="M4 7 l2 2 l4-4" stroke="var(--teal-deep)" stroke-width="1.6" fill="none"/></svg>Experienced Implant Clinician</li>
    <li><svg width="12" height="12" viewBox="0 0 14 14"><circle cx="7" cy="7" r="6" stroke="var(--teal-deep)" stroke-width="1.5" fill="none"/><path d="M4 7 l2 2 l4-4" stroke="var(--teal-deep)" stroke-width="1.6" fill="none"/></svg>Gentle, Patient-Focused Care</li>
    <li><svg width="12" height="12" viewBox="0 0 14 14"><circle cx="7" cy="7" r="6" stroke="var(--teal-deep)" stroke-width="1.5" fill="none"/><path d="M4 7 l2 2 l4-4" stroke="var(--teal-deep)" stroke-width="1.6" fill="none"/></svg>Modern Technology and Techniques</li>
  </ul>

  <div class="abs phone"><svg width="25" height="25" viewBox="0 0 24 24"><circle cx="12" cy="12" r="12" fill="var(--teal-deep)"/><path d="M8 6 l2 0 l1 3 l-1.5 1 q1 2.5 3.5 3.5 l1-1.5 l3 1 l0 2 q-1 2 -3 1.5 q-5-1.5-7-7 q-0.5-2 1.5-3z" fill="#fff"/></svg>08 9351 4276</div>
  <p class="abs web">www.<span>bravonclinic</span>.com.au</p>

  <svg class="abs clinician-photo" viewBox="0 0 223 232" role="img" aria-label="Portrait of the smiling implant clinician in dark scrubs">
    <defs>
      <linearGradient id="portraitTone" x1="0" y1="0" x2="0" y2="1">
        <stop offset="0" stop-color="var(--photo-light)"/>
        <stop offset="0.45" stop-color="#cbb6a6"/>
        <stop offset="0.75" stop-color="var(--photo-dark)"/>
      </linearGradient>
    </defs>
    <path d="M0 232 V115 C0 80 30 60 66 62 C68 22 92 0 110 0 C130 0 150 22 151 62 C190 58 223 82 223 120 V232 Z" fill="url(#portraitTone)"/>
  </svg>
  <p class="abs clinician-name">Dr<br>Elias<br>Marrow</p>
</main>
</body>
</html>
```